VERIDAX Need a luxury modern business card designed.

Need a luxury modern business card designed. refer to the uploaded files for the company name and logo in the zip file under source files. i will making my descion on monday. so please send in before then so if we need to edit we will have the time. we have a trade show coming up and im on a deadline for printer.

Target Market(s)

high end clients

Contact Information for Business Card

Company nAme and logo. Calvin Ostrow Co-Founder / Project Manager Office # 416-555-0193 Cell # 416-555-0147 VERIDAX.CA Calvin@veridax.ca

Font styles to use
Other font styles liked:
• Modern

Requirements
Must have
• Company name and logo, contact info, using the black, gold and white color scheme.

```html
<!DOCTYPE html>
<html lang="en">
<head>
<meta charset="utf-8">
<title>VERIDAX Business Card</title>
<link rel="stylesheet" href="https://fonts.googleapis.com/css2?family=Rubik:wght@400;500;700&display=swap">
<style>
  :root {
    --stage: #d9d9d9;
    --card: #2e2e2e;
    --card-edge: #262626;
    --gold: #a8955a;
    --white: #f4f4f4;
    --text: #e9e9e9;
  }
  * { margin: 0; padding: 0; box-sizing: border-box; }
  html, body {
    width: 1200px; height: 1021px; overflow: hidden;
    background: var(--stage);
    font-family: "Rubik", sans-serif;
  }
  .stage {
    width: 1200px; height: 1021px;
    display: flex; flex-direction: column; align-items: center; justify-content: center;
    gap: 40px;
  }
  .card {
    position: relative;
    width: 780px; height: 446px;
    background: var(--card);
    border: 1px solid var(--card-edge);
    box-shadow: 0 6px 18px rgba(0,0,0,0.25);
    overflow: hidden;
  }
  .brand {
    position: absolute;
    display: flex; align-items: center; gap: 16px;
    color: var(--white);
    font-weight: 400;
    letter-spacing: 0.22em;
  }
  .brand-square {
    display: block;
    background: var(--gold);
  }
  .card-front .brand { left: 96px; top: 190px; font-size: 54px; }
  .card-front .brand-square { width: 40px; height: 40px; }
  .card-back .brand { left: 60px; top: 60px; font-size: 40px; }
  .card-back .brand-square { width: 28px; height: 28px; }

  .contact-list {
    position: absolute; left: 60px; top: 250px;
    list-style: none;
    color: var(--text);
    font-size: 20px; line-height: 32px; letter-spacing: 0.02em;
  }
  .contact-list li { display: flex; align-items: center; gap: 10px; }
  .contact-icon { width: 18px; height: 18px; fill: none; stroke: var(--gold); stroke-width: 1.6; }
  .contact-icon.filled { fill: var(--gold); stroke: none; }

  .person {
    position: absolute; right: 60px; top: 110px;
    text-align: right;
  }
  .person-name { color: var(--gold); font-weight: 700; font-size: 26px; letter-spacing: 0.02em; }
  .person-title { color: var(--text); font-weight: 400; font-size: 20px; margin-top: 4px; }
</style>
</head>
<body>
<main class="stage">
  <section class="card card-front">
    <div class="brand"><span class="brand-square"></span>VERIDAX</div>
  </section>

  <section class="card card-back">
    <div class="brand"><span class="brand-square"></span>VERIDAX</div>

    <div class="person">
      <p class="person-name">Calvin Ostrow</p>
      <p class="person-title">Co-Founder / Project Manager</p>
    </div>

    <ul class="contact-list">
      <li>
        <svg class="contact-icon filled" viewBox="0 0 24 24"><path d="M6.6 10.8a15 15 0 0 0 6.6 6.6l2.2-2.2a1 1 0 0 1 1-.25 11.4 11.4 0 0 0 3.6.57 1 1 0 0 1 1 1V20a1 1 0 0 1-1 1A17 17 0 0 1 3 4a1 1 0 0 1 1-1h3.5a1 1 0 0 1 1 1c0 1.25.2 2.45.57 3.57a1 1 0 0 1-.25 1z"/></svg>
        416-555-0193
      </li>
      <li>
        <svg class="contact-icon" viewBox="0 0 24 24"><rect x="6" y="2" width="12" height="20" rx="2"/><line x1="10" y1="18" x2="14" y2="18"/></svg>
        416-555-0147
      </li>
      <li>
        <svg class="contact-icon" viewBox="0 0 24 24"><rect x="2" y="5" width="20" height="14"/><polyline points="2,5 12,13 22,5"/></svg>
        Calvin@veridax.ca
      </li>
      <li>
        <svg class="contact-icon" viewBox="0 0 24 24"><circle cx="12" cy="12" r="10"/><ellipse cx="12" cy="12" rx="4" ry="10"/><line x1="2" y1="12" x2="22" y2="12"/></svg>
        VERIDAX.CA
      </li>
    </ul>
  </section>
</main>
</body>
</html>
```